Furniture Design Website Homepage

Brief as attached- Homepage Design

Silver Heron Furniture is a national retail emporium offering high quality, unique Scandinavian furniture, lighting and accessories. We are the market leader in this space and currently have 2 Showrooms – Melbourne & Sydney.

Most recently our business model has evolved from purely importing premium, one off vintage pieces to a more scalable model of representing brands and manufacturers exclusively out of Scandinavia. These partners manufacture today which ensures us of supply & quality.

We have now started to engage scandinavian designers and/or their families to re-introduce designs that have long gone out of production. These items are put back into production under the silver heron brand, and we own the world wide rights to them.

Please ensure you use the brief files attached and the catalogue images when creating the design.

Target Market(s)

Silver Heron Furniture - where beautiful Scandinavian design meets my modern Australian life.

We want our target audience to chose Scandinavian for their homes & for us to be their brand of choice.

The current perception is that we offer beautiful design but that it doesn’t suit everyone’s home / life / style.

Also that we are more expensive than most.

Industry/Entity Type

Retail

Requirements
Must have
• The colour scheme should be red and white as per the catalogue I attached. We like the look and feel of this site www.roomwhimsy.example

The furniture is more luxurious, so we need to target the upper market with a nice sleek look that makes the furniture look expensive.

```html
<!DOCTYPE html>
<html lang="en">
<head>
<meta charset="utf-8">
<title>Silver Heron Furniture</title>
<link href="https://fonts.googleapis.com/css2?family=Ubuntu:ital,wght@0,400;0,500;1,400&family=Roboto+Condensed&family=Noto+Sans&display=swap" rel="stylesheet">
<style>
:root{
  --red:#c8200e;
  --red-dark:#a81708;
  --red-text:#c8200e;
  --ink:#222;
  --ink-soft:#444;
  --logo-ink:#3a2a26;
  --nav-ink:#3d0f06;
  --line:#d6d6d6;
  --page:#f2f2f2;
}
*{box-sizing:border-box;margin:0;padding:0}
html,body{width:1195px;height:1200px;overflow:hidden;background:#fff}
body{position:relative;font-family:"Ubuntu",sans-serif;color:var(--ink)}
.abs{position:absolute}
h1,h2,h3{font-weight:400}

/* header */
.header{left:40px;top:0;width:1120px;height:202px;background:var(--red);border-top:8px solid var(--red-dark)}
.logo{left:53px;top:88px;font:500 40px/1 "Ubuntu",sans-serif;color:var(--logo-ink);letter-spacing:-1px}
.tagline{left:292px;top:28px;font:italic 400 24px/31px "Ubuntu",sans-serif;color:#fff}
.cart{left:935px;top:18px;color:#fff;font-style:italic}
.cart-title{display:flex;align-items:center;gap:4px;font-size:19px}
.cart-meta{margin:6px 0 0 8px;font-size:13px;line-height:19px}
.cart-meta a{color:#fff}
.cart-meta .checkout{margin-left:16px}
.secure{display:flex;align-items:center;gap:8px;margin-top:6px;font:500 12px "Ubuntu",sans-serif;font-style:normal;text-decoration:underline}
.nav{left:290px;top:165px;height:37px;display:flex;font-size:14px;color:var(--nav-ink)}
.nav span{position:absolute;top:10px;white-space:nowrap}
.nav .active{top:0;left:0;width:90px;height:37px;background:#fff;border-radius:4px 4px 0 0;text-align:center;line-height:37px;color:var(--ink)}

/* panels */
.panel{left:40px;width:1120px;background:#fff;box-shadow:0 3px 4px rgba(0,0,0,.18)}
.panel-top{top:202px;height:596px}
.panel-bottom{top:812px;height:400px;box-shadow:0 -1px 3px rgba(0,0,0,.1)}

.side-title{font-size:21px;font-weight:400;color:var(--red-text);letter-spacing:.3px;white-space:nowrap}
.search-box{left:58px;top:272px;width:147px;height:25px;border:2px solid #cfcfcf;border-radius:12px;background:linear-gradient(#f4f4f4,#fff)}
.range-list{left:58px;top:350px;list-style:none;font-size:17px;line-height:28.5px;color:var(--ink-soft)}
.filter{left:56px;font-size:17px;color:var(--ink-soft);width:205px;display:flex;justify-content:space-between;align-items:center}
.select{width:94px;height:28px;border:2px solid #d2d2d2;background:#fff;position:relative}
.select::after{content:"";position:absolute;right:6px;top:9px;border-left:7px solid transparent;border-right:7px solid transparent;border-top:8px solid var(--red)}
.btn-red{background:linear-gradient(#e8412a,#c41a08);color:#fff;border-radius:6px;text-align:center;font-weight:500}
.find{left:56px;top:742px;width:206px;height:36px;line-height:36px;font-size:18px}

.intro-title{left:298px;top:238px;font-size:24px;letter-spacing:.8px;color:#333}
.intro-text{left:298px;top:285px;width:850px;font:15px/17px "Noto Sans",sans-serif;letter-spacing:.45px;color:#111}

.hero{left:299px;top:347px;width:846px;height:430px;background:#e9e9e9}
.hero-photo{left:0;top:0;width:474px;height:430px;background:linear-gradient(160deg,#8a7660 0%,#3c2f26 55%,#5a4a3c 100%)}
.cat-card{left:515px;width:319px;height:127px;border:2px solid #fff;border-radius:4px;background:linear-gradient(#f3f3f3,#d9d9d9);box-shadow:0 1px 3px rgba(0,0,0,.2)}
.cat-img{position:absolute;left:12px;top:10px;width:120px;height:104px;border-radius:4px}
.cat-name{position:absolute;right:20px;top:30px;font-size:30px;color:#333;text-align:right}
.cat-link{position:absolute;right:20px;top:70px;font-size:19px;color:var(--red-text)}

/* bottom */
.keep-text{left:62px;top:860px;width:200px;font-size:16px;line-height:17.5px;color:#111}
.join{left:61px;top:939px;width:175px;height:34px;line-height:33px;font-size:16px;letter-spacing:.4px;border-radius:4px}
.privacy{left:66px;top:984px;font-size:16px;color:#222;text-decoration:underline}
.testimonial{left:58px;top:1047px;width:202px;height:160px;border:1px solid #aaa;border-radius:3px;background:linear-gradient(135deg,#dcdcdc,#a9a9a9)}
.pencil{position:absolute;left:22px;top:14px;width:30px;height:30px;background:linear-gradient(45deg,#d9a441,#eee);border-radius:3px}
.t-head{position:absolute;left:63px;top:12px;font:500 17px/24px "Roboto Condensed",sans-serif;color:#333}
.t-head span{display:block}
.t-quote{position:absolute;left:12px;top:70px;font:italic 12px/19.5px "Noto Sans",sans-serif;color:#333;white-space:nowrap}
.qmark{position:absolute;font:700 26px/1 Georgia,serif;color:#111}

.rec-icon{left:301px;top:825px;width:34px;height:34px;background:var(--red)}
.rec-title{left:345px;top:830px;font-size:22px;color:#333}
.divider{top:868px;height:290px;border-left:1px dotted #bdbdbd}
.prod-img{top:880px;height:175px;border-radius:6px}
.prod-name{top:1091px;font:16px "Roboto Condensed",sans-serif;color:#222;white-space:nowrap}
.prod-price{top:1128px;font-size:16px;color:var(--red-text)}
.mini-btn{width:67px;height:23px;line-height:21px;text-align:center;font-size:10px;color:var(--red-text);border:1px solid #bbb;border-radius:3px;background:linear-gradient(#fff,#e2e2e2)}
.active-bar{left:746px;top:1174px;width:206px;height:4px;background:var(--red)}
</style>
</head>
<body>

<header class="abs header"></header>
<div class="abs logo">silver heron</div>
<div class="abs tagline">The best of modern and classic<br>Scandinavian design</div>

<div class="abs cart">
  <div class="cart-title">
    <svg width="32" height="26" viewBox="0 0 32 26" aria-hidden="true"><path d="M1 3h5l4 14h15l4-10H8" fill="none" stroke="#fff" stroke-width="2.5"/><circle cx="12" cy="22" r="2.5" fill="#fff"/><circle cx="24" cy="22" r="2.5" fill="#fff"/></svg>
    Shopping cart
  </div>
  <div class="cart-meta">
    Items:&nbsp; 0<br>Total:&nbsp; $0.00<br>
    <a href="#">View Cart</a><span class="checkout">Checkout</span>
  </div>
  <div class="secure">
    <svg width="14" height="20" viewBox="0 0 14 20" aria-hidden="true"><path d="M3 9V6a4 4 0 0 1 8 0v3" fill="none" stroke="#fff" stroke-width="2"/><rect x="1" y="9" width="12" height="10" fill="#111"/></svg>
    100 % Secure Shopping
  </div>
</div>

<nav class="abs nav">
  <span class="active">About Us</span>
  <span style="left:103px">Furniture Resatoration</span>
  <span style="left:268px">Media</span>
  <span style="left:343px">FAQ</span>
  <span style="left:405px">Mailing List</span>
  <span style="left:508px">Blog</span>
  <span style="left:572px">Site search</span>
  <span style="left:669px">Contact US</span>
  <span style="left:762px">Account/Login</span>
</nav>

<section class="abs panel panel-top"></section>

<h3 class="abs side-title" style="left:58px;top:238px">Product search</h3>
<div class="abs search-box"></div>
<svg class="abs" style="left:210px;top:267px" width="34" height="34" viewBox="0 0 34 34" aria-hidden="true"><circle cx="13" cy="13" r="9" fill="#fff" stroke="var(--red)" stroke-width="4"/><path d="M20 20l11 11" stroke="#111" stroke-width="5" stroke-linecap="round"/></svg>

<h3 class="abs side-title" style="left:58px;top:322px;font-size:22px;letter-spacing:.8px">Browse our range</h3>
<ul class="abs range-list"><li>Furniture</li><li>Furniture packages</li><li>Accessories</li><li>Lighting</li><li>Fabrics</li></ul>

<h3 class="abs side-title" style="left:56px;top:504px">View products by type</h3>
<div class="abs filter" style="top:538px">Room:<span class="select"></span></div>
<div class="abs filter" style="top:577px">Furniture:<span class="select"></span></div>
<div class="abs filter" style="top:616px">Designers:<span class="select"></span></div>
<div class="abs filter" style="top:655px">Brands:<span class="select"></span></div>
<div class="abs filter" style="top:693px">Accessories:<span class="select"></span></div>
<div class="abs btn-red find">Find product</div>

<h1 class="abs intro-title">Silver Heron furniture</h1>
<p class="abs intro-text">Silver Heron brings the aesthetic, craftsmanship and integrity of Scandinavian design to Australia with a stunning range of newly produced commercial furniture, lighting and accessories.</p>

<div class="abs hero">
  <div class="abs hero-photo" role="img" aria-label="Dining room interior with dark wood table, upholstered chairs and a large pendant light"></div>
  <div class="abs cat-card" style="top:12px">
    <div class="cat-img" role="img" aria-label="Red lounge armchair on wooden legs" style="background:radial-gradient(circle at 45% 45%,#c83a1c,#e9e9e9 70%)"></div>
    <div class="cat-name">Furniture</div><div class="cat-link">View Colection</div>
  </div>
  <div class="abs cat-card" style="top:149px">
    <div class="cat-img" role="img" aria-label="Light wood sideboard with drawers" style="background:radial-gradient(ellipse at 50% 50%,#c9a48a,#e6e6e6 70%)"></div>
    <div class="cat-name">Accessories</div><div class="cat-link">View Colection</div>
  </div>
  <div class="abs cat-card" style="top:286px">
    <div class="cat-img" role="img" aria-label="Black dome pendant lamp" style="background:radial-gradient(circle at 50% 60%,#1a1a1a,#e6e6e6 62%)"></div>
    <div class="cat-name">Lighting</div><div class="cat-link">View Colection</div>
  </div>
</div>

<section class="abs panel panel-bottom"></section>

<h3 class="abs side-title" style="left:60px;top:826px;font-size:22px;letter-spacing:.8px">Keep up to date</h3>
<p class="abs keep-text">Discover exclusive offers, product previews, information on sales and much more!</p>
<div class="abs btn-red join">Join our Newsletter</div>
<a class="abs privacy" href="#">We value your privacy</a>

<div class="abs testimonial">
  <div class="pencil" role="img" aria-label="Pencil icon"></div>
  <div class="t-head">WHAT OUR<span>CLIENTS SAYS?</span></div>
  <span class="qmark" style="left:10px;top:60px">&ldquo;</span>
  <p class="t-quote">&nbsp;&nbsp;&nbsp;&nbsp;&nbsp;Lorem ipsum dolor sit amet,<br>consectetur adipiscing elit.<br>Aliquam cursus facilisis nunc.</p>
  <span class="qmark" style="left:175px;top:130px">&rdquo;</span>
</div>

<div class="abs rec-icon"></div>
<h2 class="abs rec-title">Recommends</h2>

<div class="abs divider" style="left:517px"></div>
<div class="abs divider" style="left:740px"></div>
<div class="abs divider" style="left:955px"></div>

<div class="abs prod-img" role="img" aria-label="Green shell rocking chair" style="left:310px;width:190px;background:radial-gradient(ellipse at 50% 40%,#86c234,#fff 68%)"></div>
<div class="abs prod-img" role="img" aria-label="Black leather lounge chair with ottoman" style="left:530px;width:195px;background:radial-gradient(ellipse at 55% 45%,#2a2a2a,#fff 68%)"></div>
<div class="abs prod-img" role="img" aria-label="Chrome dome table lamp" style="left:790px;width:130px;background:radial-gradient(ellipse at 50% 40%,#9a9a9a,#fff 62%)"></div>
<div class="abs prod-img" role="img" aria-label="Walnut side table with drawer" style="left:975px;width:165px;background:radial-gradient(ellipse at 50% 40%,#8a6a50,#fff 68%)"></div>

<div class="abs prod-name" style="left:313px">Ray Rocker</div>
<div class="abs prod-name" style="left:538px">Easy Hour Chair</div>
<div class="abs prod-name" style="left:753px;top:1094px">Bloom-Table</div>
<div class="abs prod-name" style="left:966px">Side Table-Walnut</div>

<div class="abs prod-price" style="left:314px">$ 2,299</div>
<div class="abs prod-price" style="left:538px">$ 2,299</div>
<div class="abs prod-price" style="left:751px">$ 2,299</div>
<div class="abs prod-price" style="left:967px">$ 2,299</div>

<div class="abs mini-btn" style="left:430px;top:1092px">More details</div>
<div class="abs mini-btn" style="left:430px;top:1129px">Add to cart</div>
<div class="abs mini-btn" style="left:654px;top:1092px">More details</div>
<div class="abs mini-btn" style="left:654px;top:1129px">Add to cart</div>
<div class="abs mini-btn" style="left:868px;top:1092px">More details</div>
<div class="abs mini-btn" style="left:868px;top:1129px">Add to cart</div>
<div class="abs mini-btn" style="left:1084px;top:1092px">More details</div>
<div class="abs mini-btn" style="left:1084px;top:1129px">Add to cart</div>

<div class="abs active-bar"></div>

</body>
</html>
```